Looking for a dynamic business card for a pizzeria.

A business card with our food, logo, and space for name, title, email, website, phone. The card should convey quality, unique, amazing. On the front, I envision food photo or photos with the owners names and contact information. On the back, more food with locations, website, facebook, twitter, instagram icons. It should look polished, not cartoonish, or plain.
Target Market(s)
upscale, local food buyers, 30-50 years in age.
Industry/Entity Type
Restaurant
Contact Information for Business Card
Business Name: Crustelli, LLC
Website: www.crustelli-example.com
Back:
2 locations: (can list on the back of card)
1. Harborview
3807 Marlow Street
Alderport, WA 98001
360-555-0143
2. Cedar Knoll
1736 Quenby Street
Alderport, WA 98002
360-555-0187
front:
EDITABLE space for
Business name
Person's Name
title
2nd title
Email address
cell-phone number
Requirements
Must have
- logo
- my food photo or photos (no watermarks showing)
- locations on back
- Person contact information on front
- full bleed

```html
<!DOCTYPE html>
<html lang="en">
<head>
<meta charset="utf-8">
<title>Crustelli business card</title>
<link href="https://fonts.googleapis.com/css2?family=Open+Sans:wght@400;600;700&display=swap" rel="stylesheet">
<style>
  :root {
    --bg: #ece8e2;
    --card-white: #fbfbfa;
    --brand-red: #b81d26;
    --brand-red-dark: #8f141b;
    --brand-green: #2f6b3a;
    --ink: #3a3a3a;
    --photo-warm: #c9794f;
    --photo-meat: #b8574a;
    --photo-dough: #c4ad8f;
    --photo-greens: #7a8a3e;
    --photo-bread: #c9964c;
    --photo-flour: #d8c6b0;
  }
  * { box-sizing: border-box; margin: 0; padding: 0; }
  html, body { width: 1200px; height: 1023px; overflow: hidden; }
  body {
    background: var(--bg);
    font-family: "Open Sans", Arial, sans-serif;
    position: relative;
  }
  .card {
    position: absolute;
    left: 250px;
    width: 700px;
    height: 400px;
    overflow: hidden;
    box-shadow: 0 6px 18px rgba(0,0,0,.18);
  }
  /* Front */
  .card-front { top: 90px; background: var(--card-white); }
  .card-front .swoosh { position: absolute; inset: 0; }
  .brand {
    position: absolute;
    left: 60px; top: 70px;
    display: flex; align-items: center; gap: 16px;
  }
  .brand-dot {
    width: 56px; height: 56px; border-radius: 50%;
    background: var(--brand-red);
  }
  .brand-name {
    font-size: 52px; font-weight: 600; color: var(--brand-green);
    letter-spacing: 1px;
  }
  .person { position: absolute; left: 60px; top: 200px; }
  .person-name { font-size: 30px; font-weight: 700; color: var(--brand-green); }
  .person-title { font-size: 19px; font-weight: 400; color: var(--brand-red); margin-top: 4px; }
  .contact {
    position: absolute; right: 40px; top: 52px;
    list-style: none; text-align: right;
  }
  .contact li {
    display: flex; justify-content: flex-end; align-items: center; gap: 10px;
    font-size: 16px; color: var(--brand-green); margin-bottom: 8px;
  }
  .contact li.web { font-weight: 700; }
  .contact svg { width: 20px; height: 20px; flex: none; }

  /* Back */
  .card-back { top: 530px; background: var(--brand-red); }
  .photo-grid {
    position: absolute; left: 0; top: 0; width: 700px; height: 240px;
    display: grid; grid-template-columns: repeat(3, 1fr); grid-template-rows: 1fr 1fr;
    gap: 6px; padding: 0 0 6px 0;
  }
  .photo { border-radius: 6px; }
  .photo.oven { background: linear-gradient(135deg, #e6a45c, var(--photo-warm)); }
  .photo.salami { background: linear-gradient(135deg, #d49a8a, var(--photo-meat)); }
  .photo.dough { background: linear-gradient(135deg, #d9c4a6, var(--photo-dough)); }
  .photo.sandwich { background: linear-gradient(135deg, #d8b064, var(--photo-bread)); }
  .photo.stretching { background: linear-gradient(135deg, #e6d8c6, var(--photo-flour)); }
  .photo.salad { background: linear-gradient(135deg, #9eab4e, var(--photo-greens)); }
  .back-info {
    position: absolute; left: 0; top: 240px; width: 700px; height: 160px;
    display: flex; align-items: center; padding: 0 36px; gap: 40px;
    color: #fff;
  }
  .back-brand { display: flex; align-items: center; gap: 12px; }
  .back-brand .brand-dot { width: 40px; height: 40px; background: #fff; }
  .back-brand .brand-name { color: #fff; font-size: 38px; }
  .location { font-size: 15px; line-height: 1.35; white-space: nowrap; }
  .location-name { font-weight: 700; font-size: 16px; }
  .location-phone {
    font-weight: 700; font-size: 17px;
    display: flex; align-items: center; gap: 8px;
  }
  .location-phone svg { width: 16px; height: 16px; }
</style>
</head>
<body>

<section class="card card-front">
  <svg class="swoosh" viewBox="0 0 700 400" preserveAspectRatio="none" aria-hidden="true">
    <path d="M0 372 C 220 372, 480 300, 700 110 L700 400 L0 400 Z" fill="var(--brand-green)"/>
    <path d="M0 382 C 230 380, 500 310, 700 130 L700 400 L0 400 Z" fill="var(--card-white)"/>
    <path d="M160 400 C 360 380, 560 290, 700 150 L700 400 Z" fill="var(--brand-red)"/>
  </svg>

  <div class="brand">
    <span class="brand-dot"></span>
    <span class="brand-name">Crustelli</span>
  </div>

  <div class="person">
    <p class="person-name">Dana R. Whitlow</p>
    <p class="person-title">CEO &amp; Creative Director</p>
  </div>

  <ul class="contact">
    <li>(306) 555-0112
      <svg viewBox="0 0 20 20"><rect width="20" height="20" rx="3" fill="var(--brand-red)"/><path d="M6 4h3l1 3-2 1a7 7 0 0 0 4 4l1-2 3 1v3a1 1 0 0 1-1 1A11 11 0 0 1 5 5a1 1 0 0 1 1-1z" fill="#fff"/></svg>
    </li>
    <li>dana@crustelli-example.com
      <svg viewBox="0 0 20 20"><rect width="20" height="20" rx="3" fill="var(--brand-red)"/><rect x="4" y="6" width="12" height="8" fill="none" stroke="#fff" stroke-width="1.5"/><path d="M4 6l6 5 6-5" fill="none" stroke="#fff" stroke-width="1.5"/></svg>
    </li>
    <li class="web">www.crustelli-example.com
      <svg viewBox="0 0 20 20"><rect width="20" height="20" rx="3" fill="var(--brand-red)"/><circle cx="10" cy="10" r="6" fill="none" stroke="#fff" stroke-width="1.5"/><path d="M4 10h12M10 4c-3 3-3 9 0 12M10 4c3 3 3 9 0 12" fill="none" stroke="#fff" stroke-width="1.2"/></svg>
    </li>
  </ul>
</section>

<section class="card card-back">
  <div class="photo-grid">
    <div class="photo oven" role="img" aria-label="Food photo: peppers roasting in the oven"></div>
    <div class="photo salami" role="img" aria-label="Food photo: sliced salami"></div>
    <div class="photo dough" role="img" aria-label="Food photo: rising dough balls"></div>
    <div class="photo sandwich" role="img" aria-label="Food photo: toasted sandwich"></div>
    <div class="photo stretching" role="img" aria-label="Food photo: hands stretching pizza dough"></div>
    <div class="photo salad" role="img" aria-label="Food photo: meat with green peppers and onions"></div>
  </div>

  <div class="back-info">
    <div class="back-brand">
      <span class="brand-dot"></span>
      <span class="brand-name">Crustelli</span>
    </div>
    <div class="location">
      <p class="location-name">Harborview</p>
      <p>3807 Marlow Street</p>
      <p>Alderport, WA 98001</p>
      <p class="location-phone">360-555-0143
        <svg viewBox="0 0 20 20"><rect width="20" height="20" rx="3" fill="#fff"/><path d="M6 4h3l1 3-2 1a7 7 0 0 0 4 4l1-2 3 1v3a1 1 0 0 1-1 1A11 11 0 0 1 5 5a1 1 0 0 1 1-1z" fill="var(--brand-red)"/></svg>
      </p>
    </div>
    <div class="location">
      <p class="location-name">Cedar Knoll</p>
      <p>1736 Quenby Street</p>
      <p>Alderport, WA 98002</p>
      <p class="location-phone">360-555-0187
        <svg viewBox="0 0 20 20"><rect width="20" height="20" rx="3" fill="#fff"/><path d="M6 4h3l1 3-2 1a7 7 0 0 0 4 4l1-2 3 1v3a1 1 0 0 1-1 1A11 11 0 0 1 5 5a1 1 0 0 1 1-1z" fill="var(--brand-red)"/></svg>
      </p>
    </div>
  </div>
</section>

</body>
</html>
```